Logo Call Center Consultants
Red Otter Consultants
Project: Logo Call Center Consultants
Logo Call Center Consultants - Consulting
Creative Brief
Bright & Fun-filled
Corin Maltby
President
317 Juniper Crescent Box 82 Larchmere Cove, BC V0P 2K4
877.XXX.XXXX
cmaltby@redotterconsulting.example
redotterconsulting.example

```html
<!DOCTYPE html>
<html lang="en">
<head>
<meta charset="utf-8">
<title>Red Otter Consultants – Business Cards</title>
<link rel="stylesheet" href="https://fonts.googleapis.com/css2?family=Montserrat:ital,wght@0,400;0,700;1,400;1,700&display=swap">
<style>
  :root {
    --canvas: #e6e7e9;
    --card: #fbfbfb;
    --brand: #1f7fd6;
    --brand-dark: #0b5cb0;
    --brand-deep: #0a4f9a;
    --brand-light: #4aa6ee;
    --ink-soft: #7a7f86;
    --on-brand: #ffffff;
  }
  * { box-sizing: border-box; margin: 0; padding: 0; }
  html, body { width: 1200px; height: 838px; overflow: hidden; }
  body {
    background: var(--canvas);
    font-family: "Montserrat", Arial, sans-serif;
    position: relative;
  }
  .card {
    position: absolute;
    width: 640px;
    height: 366px;
    background: var(--card);
    box-shadow: 0 14px 30px rgba(0,0,0,.14);
    overflow: hidden;
  }
  .card--back { left: 480px; top: 60px; }
  .card--front { left: 80px; top: 412px; }

  .logo {
    display: flex;
    align-items: center;
    gap: 12px;
    color: var(--brand);
    font-weight: 700;
    font-size: 30px;
    letter-spacing: -.5px;
    line-height: 1;
    white-space: nowrap;
  }
  .logo__dot {
    width: 26px; height: 26px;
    border-radius: 50%;
    background: var(--brand);
    flex: none;
  }
  .card--back .logo { position: absolute; left: 50%; top: 140px; transform: translateX(-50%); }
  .card--back .web { position: absolute; left: 0; right: 0; top: 196px; text-align: center; }
  .card--front .logo { position: absolute; left: 48px; top: 48px; }

  .web {
    color: var(--brand);
    font-size: 14px;
    font-weight: 400;
    font-style: italic;
  }
  .holder { position: absolute; left: 48px; top: 170px; }
  .holder__name { color: var(--brand); font-size: 26px; font-weight: 700; font-style: italic; }
  .holder__title { color: var(--ink-soft); font-size: 13px; font-style: italic; margin-top: 4px; }
  .card--front .web { position: absolute; left: 48px; bottom: 40px; }

  .facets { position: absolute; right: 0; bottom: 0; width: 330px; height: 214px; }

  .contact {
    position: absolute;
    right: 18px;
    bottom: 16px;
    list-style: none;
    color: var(--on-brand);
    font-size: 12px;
    line-height: 1.2;
  }
  .contact__phones { display: flex; flex-direction: column; align-items: flex-start; margin-left: auto; width: max-content; }
  .contact li { display: flex; align-items: center; gap: 7px; margin-top: 5px; white-space: nowrap; }
  .contact svg { width: 11px; height: 11px; flex: none; }
  .contact__email { margin-top: 12px; justify-content: flex-end; }
</style>
</head>
<body>

<section class="card card--back" aria-label="Card reverse">
  <div class="logo"><span class="logo__dot"></span>Red Otter Consultants</div>
  <p class="web">www.redotterconsulting.example</p>
</section>

<section class="card card--front" aria-label="Card front">
  <div class="logo"><span class="logo__dot"></span>Red Otter Consultants</div>

  <div class="holder">
    <h1 class="holder__name">Corin Maltby</h1>
    <p class="holder__title">President</p>
  </div>

  <p class="web">www.redotterconsulting.example</p>

  <svg class="facets" viewBox="0 0 330 214" preserveAspectRatio="none" aria-hidden="true">
    <polygon points="70,0 330,0 330,214 0,214" fill="var(--brand)"/>
    <polygon points="70,0 190,0 90,214 0,214" fill="var(--brand-dark)"/>
    <polygon points="190,0 330,0 330,70 230,120" fill="var(--brand-light)"/>
    <polygon points="230,120 330,70 330,214 170,214" fill="var(--brand)"/>
    <polygon points="190,0 230,120 90,214" fill="var(--brand-deep)" opacity=".55"/>
  </svg>

  <ul class="contact">
    <li class="contact__phones">
      <ul style="list-style:none">
        <li>
          <svg viewBox="0 0 12 12"><path d="M3 1l2 2-1 1.5c.8 1.6 1.9 2.7 3.5 3.5L9 7l2 2-1.5 2C5 11 1 7 1 2.5z" fill="currentColor"/></svg>
          877.XXX.XXXX
        </li>
        <li>
          <svg viewBox="0 0 12 12"><rect x="3" y="1" width="6" height="10" rx="1.2" fill="currentColor"/></svg>
          604.555.0182
        </li>
        <li>
          <svg viewBox="0 0 12 12"><path d="M3 1l2 2-1 1.5c.8 1.6 1.9 2.7 3.5 3.5L9 7l2 2-1.5 2C5 11 1 7 1 2.5z" fill="currentColor"/></svg>
          925.555.0195
        </li>
        <li>
          <svg viewBox="0 0 12 12"><rect x="1" y="3" width="10" height="7" fill="currentColor"/><rect x="3" y="1" width="6" height="3" fill="currentColor"/></svg>
          604.555.0183
        </li>
      </ul>
    </li>
    <li class="contact__email">
      <svg viewBox="0 0 12 12"><rect x="1" y="2.5" width="10" height="7" fill="none" stroke="currentColor" stroke-width="1.2"/><path d="M1 3l5 4 5-4" fill="none" stroke="currentColor" stroke-width="1.2"/></svg>
      cmaltby@redotterconsulting.example
    </li>
  </ul>
</section>

</body>
</html>
```